Kem7Dex Letterhead

Need a new letterhead for my law firm.
IDENTIFYING INFORMATION BELOW:
Ansel T Brightwater III
Attorney at Law
Address: 4832 Tillbury Rd, Ste 250, Dallas, TX 75204
Phone: 866-402-7183
Fax: 469-583-0271
Email: kem@kem7dex.example
Website: www.kem7dex.example

Colors
0054AA
0677BA
7BADD7
CADEEF
E8F1F8

Requirements
Must have
• Logo needs to be on the letterhead, along with identifying information which is included in the project description.

```html
<!DOCTYPE html>
<html lang="en">
<head>
<meta charset="utf-8">
<title>Kem7Dex Letterhead</title>
<link rel="stylesheet" href="https://fonts.googleapis.com/css2?family=Montserrat:wght@400;700;800&family=Roboto+Condensed:wght@400&display=swap">
<style>
  :root {
    --backdrop: #3c3c3e;
    --paper: #ffffff;
    --paper-tint: #f9f9f9;
    --ink: #111111;
    --brand-blue: #1a8fd1;
    --deep-blue: #0054aa;
    --rule: #a8a8a8;
    --faint-box: #efefef;
  }
  * { margin: 0; padding: 0; box-sizing: border-box; }
  html, body { width: 849px; height: 1200px; overflow: hidden; background: var(--backdrop); }
  .canvas { position: relative; width: 849px; height: 1200px; background: var(--backdrop); }
  .letterhead {
    position: absolute; left: 68px; top: 95px; width: 713px; height: 1011px;
    background: var(--paper-tint); overflow: hidden;
  }
  .header-chevron { position: absolute; left: 0; top: 0; width: 713px; height: 180px; }
  .firm-name {
    position: absolute; left: 363px; top: 25px; width: 240px; text-align: center;
    font-family: "Montserrat", sans-serif; font-weight: 800; font-size: 30px;
    letter-spacing: 1px; color: var(--ink);
  }
  .attorney { position: absolute; left: 46px; top: 43px; font-family: "Montserrat", sans-serif; color: var(--brand-blue); }
  .attorney-name { font-weight: 700; font-size: 16.5px; line-height: 20px; }
  .attorney-title { font-weight: 400; font-size: 16.5px; line-height: 20px; }
  .contact-list { position: absolute; left: 44px; top: 87px; list-style: none;
    font-family: "Roboto Condensed", sans-serif; font-size: 13px; color: var(--ink); }
  .contact-list li { display: flex; align-items: center; height: 18.5px; }
  .contact-icon { width: 15px; height: 15px; margin-right: 5px; flex: none; }
  .contact-sep { margin-right: 6px; }
  .header-rule { position: absolute; left: 27px; top: 192px; width: 658px; height: 1px; background: var(--rule); }
  .letter-date { position: absolute; left: 563px; top: 227px; font-family: "Roboto Condensed", sans-serif; font-size: 13.5px; color: var(--ink); }
  .center-mark {
    position: absolute; left: 161px; top: 463px; width: 386px; height: 101px; background: var(--faint-box);
    display: flex; align-items: center; justify-content: center;
    font-family: "Montserrat", sans-serif; font-weight: 800; font-size: 44px; letter-spacing: 2px; color: var(--paper);
  }
  .footer-band { position: absolute; left: 0; bottom: 0; width: 713px; height: 12px; }
</style>
</head>
<body>
<div class="canvas">
  <section class="letterhead">
    <svg class="header-chevron" viewBox="0 0 713 180" aria-hidden="true">
      <defs>
        <linearGradient id="blueStroke" x1="0" y1="1" x2="1" y2="0">
          <stop offset="0" stop-color="#0054aa"/>
          <stop offset="0.5" stop-color="#1a9ae0"/>
          <stop offset="1" stop-color="#0054aa"/>
        </linearGradient>
      </defs>
      <polygon points="255,0 520,150 652,0" fill="#ffffff"/>
      <polygon points="238,0 258,0 520,150 520,165" fill="#111111"/>
      <polygon points="520,165 520,150 652,0 665,0" fill="url(#blueStroke)"/>
    </svg>
    <div class="firm-name">KEM7DEX</div>

    <div class="attorney">
      <div class="attorney-name">ANSEL T BRIGHTWATER III</div>
      <div class="attorney-title">ATTORNEY AT LAW</div>
    </div>

    <ul class="contact-list">
      <li><svg class="contact-icon" viewBox="0 0 16 16"><circle cx="8" cy="8" r="8" fill="#111"/><path d="M8 3.5a3 3 0 0 0-3 3c0 2.2 3 5.8 3 5.8s3-3.6 3-5.8a3 3 0 0 0-3-3z" fill="none" stroke="#fff" stroke-width="1.2"/><circle cx="8" cy="6.5" r="1" fill="#fff"/></svg><span class="contact-sep">|</span>4832 Tillbury Rd, Ste 250, Dallas, TX 75204</li>
      <li><svg class="contact-icon" viewBox="0 0 16 16"><circle cx="8" cy="8" r="8" fill="#111"/><path d="M5 4l2 2-1 1.2c.6 1.3 1.5 2.2 2.8 2.8L10 9l2 2-1.2 1.3C7.5 12 4 8.5 3.7 5.2z" fill="none" stroke="#fff" stroke-width="1"/></svg><span class="contact-sep">|</span>Phone: 866-402-7183</li>
      <li><svg class="contact-icon" viewBox="0 0 16 16"><circle cx="8" cy="8" r="8" fill="#111"/><rect x="4" y="6" width="8" height="6" fill="none" stroke="#fff" stroke-width="1"/><rect x="6" y="3.5" width="4" height="2.5" fill="none" stroke="#fff" stroke-width="1"/></svg><span class="contact-sep">|</span>Fax: 469-583-0271</li>
      <li><svg class="contact-icon" viewBox="0 0 16 16"><circle cx="8" cy="8" r="8" fill="#111"/><rect x="4" y="5" width="8" height="6" fill="none" stroke="#fff" stroke-width="1"/><path d="M4 5l4 3.5L12 5" fill="none" stroke="#fff" stroke-width="1"/></svg><span class="contact-sep">|</span>Email: kem@kem7dex.example</li>
      <li><svg class="contact-icon" viewBox="0 0 16 16"><circle cx="8" cy="8" r="8" fill="#111"/><circle cx="8" cy="8" r="4.5" fill="none" stroke="#fff" stroke-width="1"/><ellipse cx="8" cy="8" rx="2" ry="4.5" fill="none" stroke="#fff" stroke-width="0.9"/><path d="M3.5 8h9" stroke="#fff" stroke-width="0.9"/></svg><span class="contact-sep">|</span>Website: www.kem7dex.example</li>
    </ul>

    <div class="header-rule"></div>
    <div class="letter-date">Date: 00 /00/0000</div>

    <div class="center-mark">KEM7DEX</div>

    <svg class="footer-band" viewBox="0 0 713 12" preserveAspectRatio="none" aria-hidden="true">
      <defs>
        <linearGradient id="footerBlue" x1="0" x2="1">
          <stop offset="0" stop-color="#1a9ae0"/>
          <stop offset="0.7" stop-color="#1a8fd1"/>
          <stop offset="1" stop-color="#0054aa"/>
        </linearGradient>
      </defs>
      <polygon points="0,2 455,2 470,9 0,9" fill="#111111"/>
      <polygon points="455,2 713,2 713,9 470,9" fill="url(#footerBlue)"/>
      <rect x="0" y="10" width="713" height="1" fill="#9a9a9a"/>
    </svg>
  </section>
</div>
</body>
</html>
```